Aunt's Go Yonder - Graphic Pic for Book Cover

I need a BOOK Cover design that has Logo incorporated:
Aunt's Go Yonder
Book Size 5x7.

This is a play on the word HIGH - which really is just a feeling people may get when they are out in nature. NOT cartoon looking.

Book Cover Words:
Aunt’s Go Yonder: A Quiet Riverbank Glow
PS. No Drugs or Alcohol Needed.

I am writing an inspirational book called Aunt’s Go Yonder. It is about hard working, determined mothers with dreams of living the good life while raising successful children along the way. The only problem is that most Mother’s have so many responsibilities that they put upon themselves that sometimes they get stuck in a routine and become fearful of adventure and taking risks. As a result, women lose their sense of freedom and do not take much-needed alone time. Yet, ultimately Mother’s can learn to take a break, which can solve many problems and propel them on to a new trail that may include the high country!

HI.I am looking forward to your designs!! Added Friday, May 1, 2015

Mothers of all ages, from 18 to 80

Aunt's Go Yonder

Pictorial/Combination Logo
f68e4e
f68d4d
faa54b
ffc214
fbed22
f04a50

• Colorful, like sunset colors. Vibrant, Fun...
• Words on it:
• Aunt's Go Yonder.
• Quiet Riverbank Glow.
• P.S. No Drugs or Alcohol Needed
• I like the billboard idea with logo in it.
• Road into mountain
• Words on it: Aunt's Go Yonder. Quiet Riverbank Glow.
• The book cover, website logo all need to tie together.
• Attached are some rough ideas...that I drew up. and a image that might be able to be used.

```html
<!DOCTYPE html>
<html lang="en">
<head>
<meta charset="utf-8">
<title>Aunt's Go Yonder – Book Cover</title>
<link href="https://fonts.googleapis.com/css2?family=Pinyon+Script&family=Jim+Nightshade&family=Oswald:wght@400&display=swap" rel="stylesheet">
<style>
  :root {
    --sky-top: #8db4e3;
    --sky-mid: #c2d8ef;
    --haze: #e8efe6;
    --hill: #7d9668;
    --hill-dark: #5d7448;
    --field: #b8d46a;
    --field-bright: #d9ea8c;
    --field-deep: #5f8a2e;
    --disc: rgba(236, 242, 250, 0.72);
    --title-blue: #6d9bd3;
    --band: rgba(128, 166, 214, 0.82);
    --subtitle-yellow: #f4f0a2;
    --author-white: #ffffff;
  }
  html, body {
    margin: 0;
    padding: 0;
    width: 857px;
    height: 1200px;
    overflow: hidden;
    background: #ffffff;
  }
  .cover {
    position: relative;
    width: 857px;
    height: 1200px;
    overflow: hidden;
  }
  .cover-photo {
    position: absolute;
    inset: 0;
    background:
      radial-gradient(ellipse 260px 180px at 560px 760px, rgba(255,250,220,0.85), rgba(255,250,220,0) 70%),
      linear-gradient(to bottom,
        var(--sky-top) 0%,
        var(--sky-mid) 35%,
        var(--haze) 52%,
        var(--hill) 60%,
        var(--hill-dark) 70%,
        var(--field-bright) 82%,
        var(--field) 90%,
        var(--field-deep) 100%);
  }
  .title-disc {
    position: absolute;
    left: 113px;
    top: 41px;
    width: 630px;
    height: 630px;
    border-radius: 50%;
    background: var(--disc);
  }
  .title {
    position: absolute;
    left: 0;
    top: 0;
    width: 857px;
    margin: 0;
    font-family: "Pinyon Script", cursive;
    font-weight: 400;
    color: var(--title-blue);
    text-align: center;
  }
  .title span {
    position: absolute;
    left: 0;
    width: 857px;
    line-height: 1;
    white-space: nowrap;
  }
  .title-line-1 { top: 110px; font-size: 170px; }
  .title-line-2 { top: 275px; font-size: 135px; }
  .title-line-3 { top: 420px; font-size: 160px; }
  .subtitle-band {
    position: absolute;
    left: 0;
    top: 1035px;
    width: 857px;
    height: 112px;
    background: var(--band);
    display: flex;
    align-items: center;
    justify-content: center;
  }
  .subtitle {
    margin: 0;
    font-family: "Jim Nightshade", cursive;
    font-weight: 400;
    font-size: 66px;
    color: var(--subtitle-yellow);
    white-space: nowrap;
  }
  .author {
    position: absolute;
    left: 32px;
    top: 1152px;
    margin: 0;
    font-family: "Oswald", sans-serif;
    font-size: 34px;
    font-variant: small-caps;
    letter-spacing: 1px;
    line-height: 1;
    color: var(--author-white);
  }
</style>
</head>
<body>
  <div class="cover">
    <div class="cover-photo" role="img" aria-label="Photograph of a woman seen from behind with arms spread wide, standing in a sunlit grassy meadow facing green mountains under a blue sky"></div>
    <div class="title-disc"></div>
    <h1 class="title">
      <span class="title-line-1">Aunt’s</span>
      <span class="title-line-2">Go</span>
      <span class="title-line-3">Yonder</span>
    </h1>
    <div class="subtitle-band">
      <p class="subtitle">A Quiet Riverbank Glow</p>
    </div>
    <p class="author">By Authors Name</p>
  </div>
</body>
</html>
```